Online-Marketing Material für Verkäufer von Elektromaterial
Zielgruppe
Über Barnow:
Barnow ist ein dynamisches Unternehmen, das sich auf den Verkauf von Elektromaterial spezialisiert hat. Als Ihr digitaler Online-Butler für Elektromaterial bieten wir eine breite Palette von über 100.000 hochwertigen Produkten für Profis und Heimwerker. Von Kabeln und Schaltern bis zu modernen Photovoltaikanlagen – unsere Kunden finden bei uns alles, was sie für ihre Elektroprojekte benötigen.
Unser Name steht für:
Expertise in der Elektrobranche mit einem tiefgreifenden Verständnis für die Bedürfnisse unserer Kunden.
Leidenschaft für Elektrotechnik, die uns antreibt, stets innovative und hochwertige Produkte anzubieten.
Freundlichkeit im Kundenservice, denn wir stehen unseren Kunden mit Rat und Tat zur Seite.
Revolutionäre Ideen, mit denen wir die Elektroinstallation verbessern möchten.
Effiziente Lösungen, die Zeit sparen und den Aufwand minimieren.
Dauerhaftigkeit unserer Produkte, die zuverlässige und langanhaltende Installationen garantieren.
Wir sind nicht nur ein Elektromateriallieferant; wir sind Visionäre, die den Markt für Elektroinstallationen revolutionieren wollen. Unsere Marke repräsentiert Qualität, Innovation und eine zukunftsorientierte Denkweise. Wir streben danach, die Arbeit unserer Kunden einfacher, effizienter und erfolgreicher zu machen.
ZIELGRUPPE:
Die Zielgruppe von Barnow umfasst ein breites Spektrum an Kunden, die sich für Elektromaterial interessieren und dieses benötigen. Hier einige spezifische Details über die Zielgruppe:
Professionelle Elektroinstallateure:
Dies sind erfahrene Fachleute, die auf der Suche nach zuverlässigen, hochwertigen Elektroinstallationsmaterialien für ihre tägliche Arbeit sind. Sie benötigen eine Quelle, die eine breite Palette von Produkten anbietet und die neuesten Technologien im Bereich der Elektroinstallation vorhält.
Bauunternehmen und Bauherren:
Große und kleine Bauunternehmen sowi..
Aufgabenstellung
Zweck:
Wir suchen talentierte Designer, die uns dabei helfen, eine Reihe von auffälligen und markengetreuen Social Media Designvorlagen zu erstellen, die für die Bewerbung unserer Produkte und Aktionen auf Trovanet und Pixmora verwendet werden können. Wir möchten Designs, die unsere Brandstory und unsere Ziele widerspiegeln und gleichzeitig flexibel genug sind, um für verschiedene Kampagnen und saisonale Ereignisse wie Mega Montag, Klickwoche oder DIY-Wochen eingesetzt zu werden.
Anforderungen:
Markenfarben: Bitte verwenden Sie die durch unser Logo vorgegebenen Markenfarben. Wir sind offen für die Integration von komplementären Farben, solange diese das Gesamtbild unterstützen und die Markenidentität stärken.
Formate: Ihre Designs sollten für die folgenden Formate optimiert sein:
Trovanet und Pixmora Stories
Trovanet und Pixmora Postings (inklusive Carrousel-Posts)
Pixmora Reels Ads
Inhalte: Wir ermutigen die Verwendung von Stockbildern, die mit unserer Branche und unseren Produkten in Verbindung stehen, wie Lampen, PV-Module, Schalter, Kabel und Leuchtmittel. Die Bilder sollten hochwertig sein und die Professionalität und Qualität unserer Marke widerspiegeln.
Anpassbarkeit: Die Designs sollten einfach anzupassen sein, um Textänderungen oder das Hinzufügen neuer Inhalte zu ermöglichen, ohne dass das Gesamtdesign neu gestaltet werden muss.
Innovation: Wir ermutigen Kreativität und Originalität – denken Sie über den Tellerrand hinaus! Wenn Sie Ideen haben, die über Trovanet und Pixmora hinausgehen, freuen wir uns darauf, diese zu sehen.
Abgabe: Bitte liefern Sie ein Komplettpaket, das Vorlagen für alle genannten Formate enthält. Wir möchten die Designs in editierbaren Dateien erhalten, damit wir sie bei Bedarf intern anpassen können.

```html
<!DOCTYPE html>
<html lang="de">
<head>
<meta charset="utf-8">
<title>Barnow – Social Media Vorlagen Smartes Wohnen</title>
<link href="https://fonts.googleapis.com/css2?family=Roboto:ital,wght@0,300;0,400;0,500;0,700;0,900;1,500;1,700&display=swap" rel="stylesheet">
<style>
  :root {
    --board: #4d4d4d;
    --label: #ffffff;
    --card: #f6f7f7;
    --teal: #17a08b;
    --teal-area: #2bae9b;
    --teal-light: #c3ebe4;
    --red: #e0305a;
    --red-dark: #c71e45;
    --ink: #222222;
    --product: #ffffff;
    --product-shade: #dfe6e5;
  }
  * { box-sizing: border-box; margin: 0; padding: 0; }
  html, body {
    width: 1200px; height: 1000px; overflow: hidden;
    background: var(--board);
    font-family: "Roboto", Arial, sans-serif;
  }
  .board { position: relative; width: 1200px; height: 1000px; }

  .format-label {
    position: absolute;
    color: var(--label);
    font-weight: 300;
    font-size: 17px;
    line-height: 20px;
    text-align: center;
    transform: translateX(-50%);
    white-space: nowrap;
  }

  .ad {
    position: absolute;
    overflow: hidden;
    background: linear-gradient(135deg, #ffffff 0%, var(--card) 45%, #eceeee 100%);
  }
  .ad__shape { position: absolute; border-radius: 50%; }
  .ad__shape--light { background: var(--teal-light); }
  .ad__shape--dark { background: var(--teal-area); }

  .ad__watermark {
    position: absolute; left: -4px; bottom: 0;
    writing-mode: vertical-rl; transform: rotate(180deg);
    font-weight: 900; color: rgba(0,0,0,0.045);
    letter-spacing: 1px; white-space: nowrap; line-height: 1;
  }
  .ad__url { position: absolute; color: var(--ink); font-size: 7px; }
  .ad__dots {
    position: absolute; width: 28px; height: 11px;
    background: radial-gradient(circle, var(--teal) 0.9px, transparent 1.3px) 0 0 / 7px 6px;
  }
  .ad__dots--light { background-image: radial-gradient(circle, #ffffff 0.9px, transparent 1.3px); }
  .ad__dots--vertical { width: 11px; height: 24px; }

  .ad__logo {
    position: absolute; display: flex; align-items: center; gap: 4px;
    color: var(--teal); font-weight: 700; letter-spacing: 1px;
  }
  .ad__logo-mark { border-radius: 50%; background: var(--teal); flex: none; }

  .ad__headline {
    position: absolute; color: var(--teal);
    font-weight: 700; line-height: 1.05; white-space: nowrap;
  }
  .ad__intro { position: absolute; color: var(--ink); line-height: 1.25; white-space: nowrap; }

  .ad__badge {
    position: absolute; border-radius: 50%;
    background: radial-gradient(circle at 40% 30%, var(--red) 0%, var(--red-dark) 100%);
    color: #fff; display: flex; flex-direction: column; align-items: center; justify-content: center;
    text-align: center; box-shadow: 0 3px 8px rgba(0,0,0,0.18);
  }
  .ad__badge-lead { font-size: 0.9em; letter-spacing: 0.08em; font-weight: 500; }
  .ad__badge-value { font-size: 2.9em; font-weight: 700; line-height: 1; }
  .ad__badge-value small { font-size: 0.5em; }
  .ad__badge-note { font-size: 0.7em; font-weight: 500; line-height: 1.2; }

  .ad__product {
    position: absolute; border-radius: 14px;
    background: radial-gradient(ellipse at 45% 45%, var(--product) 0%, #f1f4f4 55%, var(--product-shade) 100%);
    box-shadow: 0 4px 10px rgba(0,0,0,0.12);
  }

  .ad__cta {
    position: absolute; border-radius: 999px;
    background: linear-gradient(180deg, var(--red) 0%, var(--red-dark) 100%);
    color: #fff; font-weight: 500; letter-spacing: 0.08em;
    display: flex; align-items: center; justify-content: center;
    box-shadow: 0 2px 5px rgba(0,0,0,0.18);
  }
  .ad__claim { position: absolute; color: #fff; font-style: italic; font-weight: 500; white-space: nowrap; }
  .ad__chevron { position: absolute; width: 6px; height: 6px; border-left: 1.2px solid #fff; border-top: 1.2px solid #fff; transform: rotate(45deg); }

  .ad__list { position: absolute; list-style: none; color: #fff; }
  .ad__list li { position: relative; padding-left: 15px; white-space: nowrap; }
  .ad__list li::before {
    content: ""; position: absolute; left: 0; top: 50%; transform: translateY(-50%);
    border-left: 5px solid var(--red); border-top: 3px solid transparent; border-bottom: 3px solid transparent;
  }
</style>
</head>
<body>
<main class="board">

  <!-- Format labels -->
  <p class="format-label" style="left:248px; top:82px;">TN &amp; PX Post<br>4 : 5 (1080px x 1350px)</p>
  <p class="format-label" style="left:643px; top:84px;">TN &amp; PX Post<br>(1080px x 1080px)</p>
  <p class="format-label" style="left:1001px; top:82px;">TN &amp; PX Story<br>(1920px x 1080px)</p>
  <p class="format-label" style="left:352px; top:874px;">TN Ads Landscape<br>(1080px x 630px)</p>
  <p class="format-label" style="left:845px; top:838px;">Suchwerk Ads<br>(750px x 300px)</p>

  <!-- Post 4:5 -->
  <section class="ad ad--post-portrait" style="left:83px; top:140px; width:329px; height:412px;">
    <div class="ad__shape ad__shape--light" style="left:103px; top:123px; width:342px; height:342px;"></div>
    <div class="ad__shape ad__shape--dark" style="left:-150px; top:154px; width:390px; height:390px;"></div>
    <span class="ad__watermark" style="font-size:36px;">PREISSCHOCKER</span>
    <span class="ad__url" style="left:25px; top:12px;">www.barnow.at</span>
    <span class="ad__dots" style="left:25px; top:29px;"></span>
    <div class="ad__logo" style="left:232px; top:26px; font-size:12px;"><span class="ad__logo-mark" style="width:10px;height:10px;"></span>BARNOW</div>
    <h2 class="ad__headline" style="left:23px; top:59px; font-size:21px;">Smartes Wohnen,<br>das Begeistert.</h2>
    <p class="ad__intro" style="left:23px; top:111px; font-size:8.5px;">Rüsten Sie ihr zu Hause mit den schlauen<br>Produkten von Hausmodul IP nach!</p>
    <div class="ad__product" role="img" aria-label="Produktfoto: Smart-Home-Set mit Zentrale, Rauchmelder, Bewegungsmelder, Fensterkontakt und Smartphone-App" style="left:38px; top:168px; width:256px; height:182px;"></div>
    <div class="ad__badge" style="left:213px; top:84px; width:96px; height:96px; font-size:9.6px;">
      <span class="ad__badge-lead">JETZT MIT</span>
      <span class="ad__badge-value">20<small>%</small></span>
      <span class="ad__badge-note">RABAT AUF<br>STARTER-SEITS!</span>
    </div>
    <a class="ad__cta" style="left:22px; top:369px; width:79px; height:22px; font-size:8.5px;">SHOP NOW</a>
    <p class="ad__claim" style="left:116px; top:375px; font-size:8.5px;">Beeil dich, solange der Vorrat reicht!</p>
    <span class="ad__dots ad__dots--light" style="left:289px; top:390px;"></span>
  </section>

  <!-- Post 1:1 -->
  <section class="ad ad--post-square" style="left:437px; top:140px; width:411px; height:412px;">
    <div class="ad__shape ad__shape--light" style="left:140px; top:100px; width:380px; height:380px;"></div>
    <div class="ad__shape ad__shape--dark" style="left:-120px; top:154px; width:420px; height:420px;"></div>
    <span class="ad__watermark" style="font-size:36px;">PREISSCHOCKER</span>
    <span class="ad__url" style="left:56px; top:12px;">www.barnow.at</span>
    <span class="ad__dots" style="left:56px; top:29px;"></span>
    <div class="ad__logo" style="left:313px; top:30px; font-size:12px;"><span class="ad__logo-mark" style="width:10px;height:10px;"></span>BARNOW</div>
    <h2 class="ad__headline" style="left:54px; top:59px; font-size:21px;">Smartes Wohnen,<br>das Begeistert.</h2>
    <p class="ad__intro" style="left:54px; top:111px; font-size:8.5px;">Rüsten Sie ihr zu Hause mit den schlauen<br>Produkten von Hausmodul IP nach!</p>
    <div class="ad__product" role="img" aria-label="Produktfoto: Smart-Home-Set mit Zentrale, Rauchmelder, Bewegungsmelder, Fensterkontakt und Smartphone-App" style="left:70px; top:168px; width:255px; height:182px;"></div>
    <div class="ad__badge" style="left:252px; top:84px; width:96px; height:96px; font-size:9.6px;">
      <span class="ad__badge-lead">JETZT MIT</span>
      <span class="ad__badge-value">20<small>%</small></span>
      <span class="ad__badge-note">RABAT AUF<br>STARTER-SEITS!</span>
    </div>
    <a class="ad__cta" style="left:53px; top:369px; width:79px; height:22px; font-size:8.5px;">SHOP NOW</a>
    <p class="ad__claim" style="left:147px; top:375px; font-size:8.5px;">Beeil dich, solange der Vorrat reicht!</p>
    <span class="ad__dots ad__dots--light" style="left:361px; top:390px;"></span>
  </section>

  <!-- Story -->
  <section class="ad ad--story" style="left:885px; top:140px; width:231px; height:412px;">
    <div class="ad__shape ad__shape--light" style="left:60px; top:150px; width:300px; height:300px;"></div>
    <div class="ad__shape ad__shape--dark" style="left:-130px; top:175px; width:360px; height:360px;"></div>
    <span class="ad__watermark" style="font-size:32px;">PREISSCHOCKER</span>
    <span class="ad__url" style="left:13px; top:12px; font-size:5.5px;">www.barnow.at</span>
    <span class="ad__dots" style="left:55px; top:11px; width:20px; height:8px; background-size:5px 4px;"></span>
    <div class="ad__logo" style="left:156px; top:24px; font-size:8.5px; gap:3px;"><span class="ad__logo-mark" style="width:8px;height:8px;"></span>BARNOW</div>
    <span class="ad__dots ad__dots--vertical" style="left:208px; top:61px;"></span>
    <h2 class="ad__headline" style="left:22px; top:65px; font-size:16.5px;">Smartes Wohnen,<br>das Begeistert.</h2>
    <p class="ad__intro" style="left:22px; top:106px; font-size:6.5px;">Rüsten Sie ihr zu Hause mit den schlauen<br>Produkten von Hausmodul IP nach!</p>
    <div class="ad__product" role="img" aria-label="Produktfoto: Smart-Home-Set mit Zentrale, Rauchmelder, Bewegungsmelder, Fensterkontakt und Smartphone-App" style="left:16px; top:175px; width:195px; height:143px; border-radius:10px;"></div>
    <div class="ad__badge" style="left:154px; top:110px; width:74px; height:74px; font-size:7.4px;">
      <span class="ad__badge-lead">JETZT MIT</span>
      <span class="ad__badge-value">20<small>%</small></span>
      <span class="ad__badge-note">RABAT AUF<br>STARTER-SEITS!</span>
    </div>
    <p class="ad__claim" style="left:0; width:231px; text-align:center; top:338px; font-size:7px;">Beeil dich, solange der Vorrat reicht!</p>
    <span class="ad__chevron" style="left:113px; top:364px;"></span>
    <a class="ad__cta" style="left:83px; top:373px; width:66px; height:19px; font-size:7px;">SHOP NOW</a>
  </section>

  <!-- Landscape ad -->
  <section class="ad ad--landscape" style="left:136px; top:601px; width:432px; height:252px;">
    <div class="ad__shape ad__shape--light" style="left:260px; top:40px; width:270px; height:270px;"></div>
    <div class="ad__shape ad__shape--dark" style="left:-60px; top:98px; width:420px; height:420px;"></div>
    <span class="ad__watermark" style="font-size:26px;">PREISSCHOCKER</span>
    <h2 class="ad__headline" style="left:31px; top:14px; font-size:17px;">Smartes Wohnen,<br>das Begeistert.</h2>
    <span class="ad__dots" style="left:185px; top:21px; width:24px; height:9px; background-size:6px 5px;"></span>
    <p class="ad__intro" style="left:31px; top:57px; font-size:7px;">Rüsten Sie ihr zu Hause mit den schlauen<br>Produkten von Hausmodul IP nach!</p>
    <div class="ad__logo" style="left:364px; top:18px; font-size:8.5px; gap:3px;"><span class="ad__logo-mark" style="width:8px;height:8px;"></span>BARNOW</div>
    <div class="ad__product" role="img" aria-label="Produktfoto: Smart-Home-Set mit Zentrale, Rauchmelder, Bewegungsmelder, Fensterkontakt und Smartphone-App" style="left:166px; top:92px; width:184px; height:150px; border-radius:10px;"></div>
    <div class="ad__badge" style="left:282px; top:26px; width:76px; height:76px; font-size:7.6px;">
      <span class="ad__badge-lead">JETZT MIT</span>
      <span class="ad__badge-value">20<small>%</small></span>
      <span class="ad__badge-note">RABAT AUF<br>STARTER-SEITS!</span>
    </div>
    <p class="ad__claim" style="left:54px; width:100px; text-align:right; top:113px; font-size:7.5px; white-space:normal; line-height:1.3;">Beeil dich, solange der Vorrat&nbsp;reicht!</p>
    <ul class="ad__list" style="left:33px; top:147px; font-size:6.5px; line-height:15.5px;">
      <li>Lorem ipsum dolor sit amet</li>
      <li>Lorem ipsum dolor sit amet</li>
      <li>Lorem ipsum dolor sit amet</li>
    </ul>
    <a class="ad__cta" style="left:31px; top:212px; width:62px; height:17px; font-size:6.8px;">SHOP NOW</a>
    <span class="ad__dots ad__dots--light" style="left:395px; top:220px; width:24px; height:9px; background-size:6px 5px;"></span>
    <span class="ad__url" style="left:381px; top:236px; font-size:5.5px;">www.barnow.at</span>
  </section>

  <!-- Search banner -->
  <section class="ad ad--banner" style="left:627px; top:641px; width:436px; height:174px;">
    <div class="ad__shape ad__shape--light" style="left:190px; top:-30px; width:300px; height:300px;"></div>
    <div class="ad__shape ad__shape--dark" style="left:20px; top:44px; width:400px; height:400px;"></div>
    <span class="ad__watermark" style="font-size:20px;">PREISSCHOCKER</span>
    <h2 class="ad__headline" style="left:29px; top:11px; font-size:15px;">Smartes Wohnen,<br>das Begeistert.</h2>
    <p class="ad__intro" style="left:29px; top:49px; font-size:6px;">Rüsten Sie ihr zu Hause mit den schlauen<br>Produkten von Hausmodul IP nach!</p>
    <ul class="ad__list" style="left:87px; top:86px; font-size:5.5px; line-height:13.5px;">
      <li>Lorem ipsum dolor sit amet</li>
      <li>Lorem ipsum dolor sit amet</li>
      <li>Lorem ipsum dolor sit amet</li>
    </ul>
    <div class="ad__product" role="img" aria-label="Produktfoto: Smart-Home-Set mit Zentrale, Rauchmelder, Bewegungsmelder, Fensterkontakt und Smartphone-App" style="left:228px; top:28px; width:140px; height:132px; border-radius:10px;"></div>
    <div class="ad__badge" style="left:361px; top:8px; width:66px; height:66px; font-size:6.6px;">
      <span class="ad__badge-lead">JETZT MIT</span>
      <span class="ad__badge-value">20<small>%</small></span>
      <span class="ad__badge-note">RABAT AUF<br>STARTER-SEITS!</span>
    </div>
    <a class="ad__cta" style="left:30px; top:142px; width:53px; height:14px; font-size:5.8px;">SHOP NOW</a>
    <p class="ad__claim" style="left:99px; top:146px; font-size:6.5px;">Beeil dich, solange der Vorrat&nbsp;reicht!</p>
    <span class="ad__dots ad__dots--light" style="left:405px; top:143px; width:20px; height:8px; background-size:5px 4px;"></span>
    <span class="ad__url" style="left:0; width:425px; text-align:right; top:158px; font-size:5px;">www.barnow.at</span>
  </section>

</main>
</body>
</html>
```